Double-sided Business card design needed

I work as an independent consultant in a range of fields, and I need a business card to describes the two main business operations in a two-sided format:

(1) HOPE - Health Outreach Peer Engagement

(2) ROOT - Restoring Original Territories Together

My personal profile so far has been describing myself as:
Dr Calvin Marsh- Independent R&D Consultant in Community Wellbeing, Education, Mental Health and Disability Support Reform

Industry/Entity Type

Business

Contact Information for Business Card

I need a double-sided business card, describing two different but related businesses that I operate: one in Disability & Mental Health, Education and Community Wellbeing consulting, teaching and research; the other in Indigenous/First Nations-specific community cultural development

Logo Text

See the two business names below for logo text - and they need two different logo designs

Logo styles of interest
Pictorial/Combination Logo

```html
<!DOCTYPE html>
<html lang="en">
<head>
<meta charset="utf-8">
<title>HOPE / ROOT Business Card Concepts</title>
<link rel="stylesheet" href="https://fonts.googleapis.com/css2?family=Open+Sans:wght@400;600&family=Arimo:wght@400;700&display=swap">
<style>
  :root {
    --paper: #ffffff;
    --card-edge: #2b2b2b;
    --teal-dark: #2e9c94;
    --teal: #6fcbc8;
    --teal-light: #b9e4e3;
    --sky: #29a8e0;
    --blue: #3c7ac4;
    --blue-light: #8fb6e6;
    --orange: #efa21e;
    --cream: #fdf1de;
    --ink: #111111;
  }
  html, body {
    margin: 0;
    padding: 0;
    width: 900px;
    height: 1200px;
    overflow: hidden;
    background: var(--paper);
  }
  .sheet {
    position: relative;
    width: 900px;
    height: 1200px;
  }
  .card {
    position: absolute;
    width: 413px;
    height: 238px;
    box-sizing: border-box;
    border: 1px solid var(--card-edge);
    background: var(--paper);
  }
  .card svg { display: block; width: 411px; height: 236px; }
  .card--hope-a { left: 26px;  top: 42px; }
  .card--hope-b { left: 457px; top: 42px; }
  .card--hope-c { left: 26px;  top: 299px; }
  .card--hope-d { left: 457px; top: 299px; }
  .card--root-a { left: 26px;  top: 595px; }
  .card--root-b { left: 457px; top: 595px; }
  .card--root-c { left: 26px;  top: 852px; }

  .tagline { font-family: "Open Sans", sans-serif; font-size: 17px; }
  .tagline--hope { fill: var(--sky); }
  .tagline--root { fill: var(--orange); }
  .tagline--root-outline { fill: var(--blue); }
  .tagline--on-band { fill: #ffffff; }

  .brand { font-family: "Open Sans", sans-serif; font-size: 17px; font-weight: 600; }
  .brand--hope { fill: var(--teal); }
  .brand--root { fill: var(--blue); }

  .holder-name { font-family: "Arimo", sans-serif; font-weight: 700; font-size: 14px; }
  .holder-name--hope { fill: var(--teal); }
  .holder-name--root { fill: var(--orange); }

  .holder-role { font-family: "Arimo", sans-serif; font-size: 12.4px; fill: var(--ink); letter-spacing: -0.25px; }
  .holder-role--small { font-size: 11.2px; }

  .fill-teal-dark { fill: var(--teal-dark); }
  .fill-teal { fill: var(--teal); }
  .fill-teal-light { fill: var(--teal-light); }
  .fill-blue { fill: var(--blue); }
  .fill-blue-light { fill: var(--blue-light); }
  .fill-orange { fill: var(--orange); }
  .fill-cream { fill: var(--cream); }
  .frame-blue { fill: none; stroke: var(--blue); stroke-width: 1.2; }
</style>
</head>
<body>
<main class="sheet">

  <!-- HOPE, wave rising behind name -->
  <div class="card card--hope-a">
    <svg viewBox="0 0 411 236">
      <rect class="fill-teal-dark" x="17" y="16" width="379" height="6"/>
      <circle class="fill-teal" cx="30" cy="68" r="6"/>
      <text class="brand brand--hope" x="40" y="74">HOPE</text>
      <text class="tagline tagline--hope" x="100" y="64">Health Outreach Peer</text>
      <text class="tagline tagline--hope" x="100" y="85">Engagement</text>
      <path class="fill-teal-light" d="M17,173 C150,170 250,131 396,130 L396,163 C260,163 150,180 17,181 Z"/>
      <text class="holder-name holder-name--hope" x="386" y="179" text-anchor="end">Dr Calvin Marsh</text>
      <text class="holder-role" x="386" y="197" text-anchor="end">Independent R&amp;D Consultant in Community Wellbeing, Education,</text>
      <text class="holder-role" x="386" y="215" text-anchor="end">Mental Health and Disability Support Reform</text>
    </svg>
  </div>

  <!-- HOPE, wave below details -->
  <div class="card card--hope-b">
    <svg viewBox="0 0 411 236">
      <rect class="fill-teal-dark" x="17" y="16" width="379" height="6"/>
      <circle class="fill-teal" cx="30" cy="68" r="6"/>
      <text class="brand brand--hope" x="40" y="74">HOPE</text>
      <text class="tagline tagline--hope" x="100" y="64">Health Outreach Peer</text>
      <text class="tagline tagline--hope" x="100" y="85">Engagement</text>
      <text class="holder-name holder-name--hope" x="386" y="144" text-anchor="end">Dr Calvin Marsh</text>
      <text class="holder-role" x="386" y="162" text-anchor="end">Independent R&amp;D Consultant in Community Wellbeing, Education,</text>
      <text class="holder-role" x="386" y="180" text-anchor="end">Mental Health and Disability Support Reform</text>
      <path class="fill-teal-light" d="M17,173 C120,174 250,212 396,218 L396,223 C250,223 120,210 17,206 Z"/>
    </svg>
  </div>

  <!-- HOPE, double top rule -->
  <div class="card card--hope-c">
    <svg viewBox="0 0 411 236">
      <rect class="fill-teal-dark" x="17" y="16" width="379" height="6"/>
      <rect class="fill-teal" x="17" y="25" width="379" height="4"/>
      <circle class="fill-teal" cx="30" cy="68" r="6"/>
      <text class="brand brand--hope" x="40" y="74">HOPE</text>
      <text class="tagline tagline--hope" x="100" y="64">Health Outreach Peer</text>
      <text class="tagline tagline--hope" x="100" y="85">Engagement</text>
      <text class="holder-name holder-name--hope" x="386" y="156" text-anchor="end">Dr Calvin Marsh</text>
      <text class="holder-role" x="386" y="174" text-anchor="end">Independent R&amp;D Consultant in Community Wellbeing, Education,</text>
      <text class="holder-role" x="386" y="192" text-anchor="end">Mental Health and Disability Support Reform</text>
      <path class="fill-teal-light" d="M17,194 C200,188 300,218 396,215 L396,222 L17,222 Z"/>
    </svg>
  </div>

  <!-- HOPE, banner with stripe field -->
  <div class="card card--hope-d">
    <svg viewBox="0 0 411 236">
      <defs>
        <linearGradient id="stripe-field" x1="0" y1="0" x2="1" y2="0">
          <stop offset="0" stop-color="#cfeef0"/>
          <stop offset="1" stop-color="#ffffff"/>
        </linearGradient>
      </defs>
      <rect x="17" y="16" width="130" height="206" fill="url(#stripe-field)" role="img" aria-label="Faint diagonal stripe pattern in pale teal"/>
      <circle class="fill-teal" cx="30" cy="68" r="6"/>
      <text class="brand brand--hope" x="40" y="74">HOPE</text>
      <rect class="fill-teal" x="92" y="46" width="288" height="44" rx="3"/>
      <text class="tagline tagline--on-band" x="100" y="64">Health Outreach Peer</text>
      <text class="tagline tagline--on-band" x="100" y="85">Engagement</text>
      <text class="holder-name holder-name--hope" x="386" y="178" text-anchor="end">Dr Calvin Marsh</text>
      <text class="holder-role" x="386" y="196" text-anchor="end">Independent R&amp;D Consultant in Community Wellbeing, Education,</text>
      <text class="holder-role" x="386" y="214" text-anchor="end">Mental Health and Disability Support Reform</text>
    </svg>
  </div>

  <!-- ROOT, top swoosh -->
  <div class="card card--root-a">
    <svg viewBox="0 0 411 236">
      <rect class="fill-orange" x="17" y="16" width="379" height="6"/>
      <path class="fill-blue-light" d="M140,22 C250,22 300,52 396,52 L396,48 C300,48 250,22 140,22 Z"/>
      <path class="fill-blue" d="M140,22 C250,22 300,48 396,48 L396,22 Z"/>
      <rect class="fill-blue" x="24" y="62" width="12" height="12"/>
      <text class="brand brand--root" x="42" y="74">ROOT</text>
      <text class="tagline tagline--root" x="100" y="64">Restoring Original Territories</text>
      <text class="tagline tagline--root" x="100" y="85">Together</text>
      <rect class="fill-cream" x="17" y="150" width="379" height="72" role="img" aria-label="Faint cream geometric pattern"/>
      <text class="holder-name holder-name--root" x="23" y="177">Dr Calvin Marsh</text>
      <text class="holder-role" x="23" y="195">Independent R&amp;D Consultant in Community Wellbeing, Education,</text>
      <text class="holder-role" x="23" y="213">Mental Health and Disability Support Reform</text>
    </svg>
  </div>

  <!-- ROOT, blue banner -->
  <div class="card card--root-b">
    <svg viewBox="0 0 411 236">
      <rect class="fill-blue" x="24" y="62" width="12" height="12"/>
      <text class="brand brand--root" x="42" y="74">ROOT</text>
      <rect class="fill-blue" x="92" y="45" width="276" height="45"/>
      <text class="tagline tagline--on-band" x="100" y="64">Restoring Original Territories</text>
      <text class="tagline tagline--on-band" x="100" y="85">Together</text>
      <rect class="fill-cream" x="17" y="150" width="379" height="63" role="img" aria-label="Faint cream geometric pattern"/>
      <text class="holder-name holder-name--root" x="23" y="166">Dr Calvin Marsh</text>
      <text class="holder-role" x="23" y="184">Independent R&amp;D Consultant in Community Wellbeing, Education,</text>
      <text class="holder-role" x="23" y="202">Mental Health and Disability Support Reform</text>
      <rect class="fill-orange" x="17" y="213" width="379" height="6"/>
    </svg>
  </div>

  <!-- ROOT, outlined frame with arc base -->
  <div class="card card--root-c">
    <svg viewBox="0 0 411 236">
      <rect class="frame-blue" x="25" y="62" width="12" height="12"/>
      <text class="brand brand--root" x="42" y="74">ROOT</text>
      <rect class="frame-blue" x="100" y="36" width="277" height="47"/>
      <text class="tagline tagline--root-outline" x="108" y="55">Restoring Original Territories</text>
      <text class="tagline tagline--root-outline" x="108" y="76">Together</text>
      <text class="holder-name holder-name--root" x="396" y="148" text-anchor="end">Dr Calvin Marsh</text>
      <text class="holder-role holder-role--small" x="396" y="164" text-anchor="end">Independent R&amp;D Consultant in Community Wellbeing, Education,</text>
      <text class="holder-role holder-role--small" x="396" y="180" text-anchor="end">Mental Health and Disability Support Reform</text>
      <path class="fill-orange" d="M17,210 Q206,183 396,210 L396,214 Q206,189 17,214 Z"/>
      <path class="fill-blue" d="M17,214 Q206,189 396,214 L396,222 L17,222 Z"/>
    </svg>
  </div>

</main>
</body>
</html>
```